business card design for luxurious real estate brand

using the attached logo, i am looking for a 2-sided business card design. the back should be the gold logo on black background. the front needs to include: gold logo, name, phone, email, and website

Industry/Entity Type

real estate

Contact Information for Business Card

logo, name, email, phone, website

Font styles to use
Sans Serif

```html
<!DOCTYPE html>
<html lang="en">
<head>
<meta charset="utf-8">
<title>Casa Verano — Business Card</title>
<link href="https://fonts.googleapis.com/css2?family=Encode+Sans+Semi+Condensed:wght@400;600;700&display=swap" rel="stylesheet">
<style>
  :root {
    --backdrop: #7f9cc0;
    --card-black: #151515;
    --card-black-soft: #262626;
    --card-white: #f7f7f7;
    --gold: #f2c318;
    --gold-light: #ffe066;
    --ink: #4a4a4a;
    --ink-dark: #2b2b2b;
    --label-grey: #9a9a9a;
  }
  * { box-sizing: border-box; margin: 0; padding: 0; }
  html, body {
    width: 1200px; height: 876px; overflow: hidden;
    background: var(--backdrop);
    font-family: "Encode Sans Semi Condensed", "Arial Narrow", sans-serif;
  }
  .canvas {
    position: relative; width: 1200px; height: 876px;
    display: flex; flex-direction: column; align-items: center; justify-content: center; gap: 48px;
  }
  .card {
    position: relative; width: 620px; height: 354px; overflow: hidden;
    box-shadow: 0 10px 28px rgba(20, 35, 60, 0.35);
  }

  /* Back side */
  .card-back .texture {
    position: absolute; inset: 0;
    background: radial-gradient(ellipse at 50% 45%, var(--card-black-soft) 0%, var(--card-black) 70%);
  }
  .card-back .gold-edge {
    position: absolute; left: 0; right: 0; top: 0; height: 10px;
    background: linear-gradient(90deg, var(--gold), var(--gold-light), var(--gold));
  }
  .brand {
    position: absolute; left: 50%; top: 50%; transform: translate(-50%, -50%);
    display: flex; align-items: center; gap: 16px;
  }
  .brand-square { width: 26px; height: 26px; background: var(--gold); }
  .brand-name {
    color: var(--gold); font-weight: 600; font-size: 30px; letter-spacing: 6px; text-transform: uppercase;
  }

  /* Front side */
  .card-front { display: flex; }
  .contact-panel {
    position: relative; width: 47%; height: 100%; background: var(--card-white);
    padding: 38px 30px 30px 34px; color: var(--ink);
  }
  .address { font-size: 17px; line-height: 1.3; }
  .website {
    position: absolute; left: 34px; bottom: 120px;
    font-size: 12px; font-weight: 700; letter-spacing: 2px; color: var(--ink-dark); text-transform: uppercase;
  }
  .direct { position: absolute; left: 34px; bottom: 34px; font-size: 20px; line-height: 1.2; }
  .name-panel {
    position: relative; flex: 1; height: 100%;
    background: radial-gradient(ellipse at 35% 45%, var(--card-black-soft) 0%, var(--card-black) 75%);
    display: flex; flex-direction: column; align-items: center; justify-content: center;
  }
  .gold-tab {
    position: absolute; left: -32px; width: 64px; height: 12px;
    background: linear-gradient(90deg, var(--gold), var(--gold-light));
  }
  .gold-tab.top { top: 0; }
  .gold-tab.bottom { bottom: 0; }
  .person-name {
    color: #fff; font-size: 30px; font-weight: 600; letter-spacing: 5px; text-transform: uppercase;
  }
  .divider { width: 22px; height: 3px; background: var(--gold); margin: 10px 0 8px; }
  .person-role { color: var(--label-grey); font-size: 14px; letter-spacing: 2px; text-transform: uppercase; }
</style>
</head>
<body>
  <main class="canvas">
    <section class="card card-back" aria-label="Card back">
      <div class="texture" role="img" aria-label="Dark background with a faint repeating brand pattern"></div>
      <div class="gold-edge"></div>
      <div class="brand">
        <span class="brand-square"></span>
        <span class="brand-name">Casa Verano</span>
      </div>
    </section>

    <section class="card card-front" aria-label="Card front">
      <div class="contact-panel">
        <p class="address">1187 Harbor Lane, Fairview<br>California - 90210</p>
        <p class="website">www.casaverano.com</p>
        <p class="direct">hello@casaverano.com<br>555-014-2290</p>
      </div>
      <div class="name-panel" role="img" aria-label="Dark panel with a faint repeating brand pattern">
        <span class="gold-tab top"></span>
        <span class="gold-tab bottom"></span>
        <h1 class="person-name">Marcus Hale</h1>
        <span class="divider"></span>
        <p class="person-role">Realtor</p>
      </div>
    </section>
  </main>
</body>
</html>
```